Print Design For Sign

Same dimensions as PDF attachment (POI8194 ReedWarbler) which is from a previous project.

Content

Sub Heading:
A collection of 20 architecturally designed apartments and villas
offering affordable, contemporary beachside living.

Bubble:
STAGE 1 SELLING FAST!

Bullet points
• Indoor/outdoor living with large alfresco
entertaining decks
• State of the art kitchens with high gloss cabinets
and stone bench tops
• Bamboo hardwood floors
• Plunge pools to selected units
• Fully fenced lots with attractive low maintenance landscaping

Contact info:

Sales enquiries: Morven Clague 0417 362 905 / morven@tbrg.com.au / www.tbrg.com.au

Then please include attached images and logos

```html
<!DOCTYPE html>
<html lang="en">
<head>
<meta charset="utf-8">
<title>Saltmere – Stage 1 Sign</title>
<link rel="stylesheet" href="https://fonts.googleapis.com/css2?family=Montserrat:ital,wght@0,400;0,600;0,700;0,800;1,500;1,700&display=swap">
<style>
  :root {
    --teal: #1d6d79;
    --teal-deep: #155a66;
    --glow: #ffffff;
    --navy: #10273a;
    --yellow: #f6d365;
    --gold: #f4b41a;
    --white: #ffffff;
    --rule: rgba(255,255,255,0.55);
    --brand: #1b6a77;
  }
  * { margin: 0; padding: 0; box-sizing: border-box; }
  html, body { width: 1200px; height: 629px; overflow: hidden; }
  body { font-family: "Montserrat", Arial, sans-serif; }
  .sign {
    position: relative; width: 1200px; height: 629px; overflow: hidden;
    background:
      radial-gradient(ellipse 360px 250px at 170px 540px, var(--glow) 0%, rgba(255,255,255,0.85) 30%, rgba(255,255,255,0.2) 70%, rgba(255,255,255,0) 100%),
      linear-gradient(180deg, var(--teal) 0%, var(--teal-deep) 100%);
  }
  .headline {
    position: absolute; left: 60px; top: 50px; width: 940px;
    color: var(--white); font-size: 33px; font-weight: 400;
    line-height: 44px; letter-spacing: 0.2px; text-transform: uppercase;
    white-space: nowrap;
  }
  .headline strong { font-weight: 800; }
  .badge {
    position: absolute; left: 996px; top: 28px; width: 158px; height: 158px;
  }
  .badge-text {
    position: absolute; left: 996px; top: 62px; width: 158px;
    text-align: center; font-weight: 800; font-size: 24px; line-height: 29px;
    color: var(--white); text-transform: uppercase;
  }
  .badge-text .stage { color: var(--yellow); display: block; }
  .gallery-frame {
    position: absolute; top: 208px; height: 191px;
    border: 3px solid var(--white); background: var(--white);
  }
  .gallery-frame .fill { width: 100%; height: 100%; }
  .frame-map { left: 35px; width: 312px; }
  .frame-map .fill { background: linear-gradient(180deg, #5d8fa0 0%, #8b7a52 35%, #b0593a 100%); }
  .frame-plan { left: 354px; width: 260px; }
  .frame-plan .fill { background: linear-gradient(160deg, #9aa7a3 0%, #c9ccc8 45%, #e5e6e3 100%); }
  .frame-render { left: 621px; width: 546px; }
  .frame-render .fill { background: linear-gradient(180deg, #ffffff 0%, #e9eef0 30%, #8f969a 60%, #7d9560 100%); }
  .brand {
    position: absolute; left: 40px; top: 520px; width: 290px;
    display: flex; align-items: center; gap: 12px;
    color: var(--brand); font-weight: 600; font-size: 38px; letter-spacing: 1px;
  }
  .brand-dot { width: 30px; height: 30px; border-radius: 50%; background: var(--gold); flex: none; }
  .features {
    position: absolute; left: 413px; top: 455px; width: 744px;
    display: flex; list-style: none;
  }
  .feature {
    position: relative; flex: none; padding: 0 4px; text-align: center;
    color: var(--yellow); font-weight: 700; font-size: 14px; line-height: 22px;
    white-space: nowrap;
  }
  .feature:nth-child(1) { width: 170px; }
  .feature:nth-child(2) { width: 177px; }
  .feature:nth-child(3) { width: 103px; }
  .feature:nth-child(4) { width: 122px; }
  .feature:nth-child(5) { width: 172px; }
  .feature + .feature::before {
    content: ""; position: absolute; left: 0; top: 0; bottom: 0;
    width: 1px; background: var(--rule);
  }
  .feature + .feature::after {
    content: ""; position: absolute; left: -2px; top: 40px;
    width: 5px; height: 5px; border-radius: 50%; background: var(--white);
  }
  .contact-rule {
    position: absolute; left: 398px; top: 557px; width: 762px; height: 1px; background: var(--rule);
  }
  .contact {
    position: absolute; left: 398px; top: 574px; width: 770px;
    color: var(--white); font-style: italic; font-weight: 500; font-size: 15.5px; white-space: nowrap;
  }
  .contact strong { font-weight: 700; }
</style>
</head>
<body>
<main class="sign">
  <h1 class="headline">A collection of <strong>20 architecturally designed</strong><br><strong>apartments and villas</strong> offering affordable,<br>contemporary beachside living.</h1>

  <svg class="badge" viewBox="0 0 158 158" aria-hidden="true">
    <circle cx="79" cy="79" r="77" fill="var(--navy)"/>
    <path d="M112 9 Q140 20 152 50 Q132 44 124 34 Q116 24 112 9 Z" fill="var(--gold)"/>
  </svg>
  <p class="badge-text"><span class="stage">Stage 1</span>Selling<br>Fast!</p>

  <figure class="gallery-frame frame-map"><div class="fill" role="img" aria-label="Aerial photo of the site with labelled town centre, airport, supermarket and bay"></div></figure>
  <figure class="gallery-frame frame-plan"><div class="fill" role="img" aria-label="Site plan showing the lots of stages 1 to 4"></div></figure>
  <figure class="gallery-frame frame-render"><div class="fill" role="img" aria-label="Rendering of the villas with carports, fences and landscaping"></div></figure>

  <div class="brand"><span class="brand-dot"></span><span>SALTMERE</span></div>

  <ul class="features">
    <li class="feature">Indoor/outdoor<br>living with<br>large alfresco<br>entertaining decks</li>
    <li class="feature">State of the art<br>kitchens with high<br>gloss cabinets and<br>stone bench tops</li>
    <li class="feature">Bamboo<br>hardwood<br>floors</li>
    <li class="feature">Plunge pools<br>to selected<br>units</li>
    <li class="feature">Fully fenced lots<br>with attractive<br>low maintenance<br>landscaping</li>
  </ul>

  <div class="contact-rule"></div>
  <p class="contact">Sales enquiries: <strong>Morven Clague 0417 362 905</strong> / morven@tbrg.com.au / www.tbrg.com.au</p>
</main>
</body>
</html>
```